Brightmoor Partners Branding Revamp

We are a consulting company, looking for a way to display and promote our brand. We have 2 sides to the business- Brightmoor (financial) and Partners (cyber security). The financial side products relate to business necessities: card processing, website design/hosting/maintenance, VoIP phone systems. The cyber security side promotes a bundled package of 4 solutions: network vulnerability scan, dark web scan, anti-ransomeware/malware software, and image-level backups. We want people to understand that partnering with Brightmoor Partners gives them “Steady Confidence Ahead” (tagline). Current badge and logos uploaded.

Target Market(s)

Small businesses

Contact Information for Business Card

Lena Marwick, Vice President, lena@brightmoorpartners.example, 555-806-1937, www.brightmoorpartners.example

Requirements
Nice to have
• I do prefer the darker background for front and back

```html
<!DOCTYPE html>
<html lang="en">
<head>
<meta charset="UTF-8">
<title>Brightmoor Partners — Business Card</title>
<link href="https://fonts.googleapis.com/css2?family=Montserrat:wght@400;500;600;700;800&display=swap" rel="stylesheet">
<style>
  :root {
    --canvas: #ffffff;
    --card: #060607;
    --red: #e3232b;
    --white: #ffffff;
    --soft-white: #f2f2f2;
  }
  * { margin: 0; padding: 0; box-sizing: border-box; }
  html, body {
    width: 1200px; height: 1000px; overflow: hidden;
    background: var(--canvas);
    font-family: "Montserrat", Arial, sans-serif;
  }
  .canvas { position: relative; width: 1200px; height: 1000px; }
  .card {
    position: absolute; left: 314px; width: 572px; height: 327px;
    background: var(--card);
  }
  .card--front { top: 157px; }
  .card--back { top: 517px; height: 326px; }

  /* Brand lockup */
  .brand { position: absolute; text-align: center; color: var(--white); }
  .brand__mark { background: var(--red); margin: 0 auto; }
  .brand__name { font-weight: 600; white-space: nowrap; line-height: 1; }
  .brand__tagline { font-weight: 500; white-space: nowrap; line-height: 1; }

  .card--front .brand { left: 0; right: 0; top: 58px; }
  .card--front .brand__mark { width: 80px; height: 80px; margin-bottom: 54px; }
  .card--front .brand__name { font-size: 26px; letter-spacing: 0.2em; margin-left: 0.2em; }
  .card--front .brand__tagline { font-size: 11px; letter-spacing: 0.34em; margin-left: 0.34em; margin-top: 34px; }

  .card--back .brand { left: 36px; width: 180px; top: 115px; }
  .card--back .brand__mark { width: 36px; height: 36px; margin-bottom: 24px; }
  .card--back .brand__name { font-size: 11px; letter-spacing: 0.16em; margin-left: 0.16em; }
  .card--back .brand__tagline { font-size: 5.5px; letter-spacing: 0.28em; margin-left: 0.28em; margin-top: 12px; }

  /* Person */
  .person { position: absolute; right: 40px; top: 57px; text-align: right; }
  .person__name { color: var(--red); font-size: 26px; font-weight: 800; line-height: 1; }
  .person__title { color: var(--white); font-size: 13px; font-weight: 700; letter-spacing: 0.1em; margin-top: 6px; line-height: 1.2; }

  .rule { position: absolute; right: 40px; width: 192px; display: flex; }
  .rule__white { flex: 1; background: var(--soft-white); }
  .rule__red { width: 39px; background: var(--red); }
  .rule--accent { top: 114px; height: 5px; }
  .rule--divider { height: 2px; }

  /* Contacts */
  .contact {
    position: absolute; right: 40px; display: flex; align-items: center; gap: 12px;
    color: var(--white); font-size: 15px; font-weight: 500;
  }
  .contact__icon {
    width: 31px; height: 31px; border-radius: 50%; background: var(--red);
    display: flex; align-items: center; justify-content: center;
  }
  .contact__icon svg { width: 17px; height: 17px; }
</style>
</head>
<body>
<div class="canvas">

  <section class="card card--front">
    <div class="brand">
      <div class="brand__mark"></div>
      <div class="brand__name">BRIGHTMOOR PARTNERS</div>
      <div class="brand__tagline">STEADY CONFIDENCE AHEAD</div>
    </div>
  </section>

  <section class="card card--back">
    <div class="brand">
      <div class="brand__mark"></div>
      <div class="brand__name">BRIGHTMOOR PARTNERS</div>
      <div class="brand__tagline">STEADY CONFIDENCE AHEAD</div>
    </div>

    <div class="person">
      <div class="person__name">LENA MARWICK</div>
      <div class="person__title">VICE PRESIDENT</div>
    </div>
    <div class="rule rule--accent"><span class="rule__white"></span><span class="rule__red"></span></div>

    <div class="contact" style="top:158px">
      <span>555-806-1937</span>
      <span class="contact__icon">
        <svg viewBox="0 0 24 24" fill="#fff"><path d="M6.6 10.8a15.1 15.1 0 0 0 6.6 6.6l2.2-2.2a1 1 0 0 1 1-.25 11.4 11.4 0 0 0 3.6.57 1 1 0 0 1 1 1V20a1 1 0 0 1-1 1A17 17 0 0 1 3 4a1 1 0 0 1 1-1h3.5a1 1 0 0 1 1 1c0 1.250.2 2.450.57 3.57a1 1 0 0 1-.25 1z"/></svg>
      </span>
    </div>
    <div class="rule rule--divider" style="top:196px"><span class="rule__white"></span><span class="rule__red"></span></div>

    <div class="contact" style="top:205px">
      <span>www.brightmoorpartners.example</span>
      <span class="contact__icon">
        <svg viewBox="0 0 24 24" fill="none" stroke="#fff" stroke-width="1.6"><circle cx="12" cy="12" r="9"/><ellipse cx="12" cy="12" rx="4" ry="9"/><path d="M3 12h18M4.5 7.5h15M4.5 16.5h15"/></svg>
      </span>
    </div>
    <div class="rule rule--divider" style="top:244px"><span class="rule__white"></span><span class="rule__red"></span></div>

    <div class="contact" style="top:254px">
      <span>lena@brightmoorpartners.example</span>
      <span class="contact__icon">
        <svg viewBox="0 0 24 24" fill="none" stroke="#fff" stroke-width="1.6"><rect x="3" y="6" width="18" height="12"/><path d="M3 6l9 7 9-7M3 18l7-6M21 18l-7-6"/></svg>
      </span>
    </div>
  </section>

</div>
</body>
</html>
```